security services Business Card Design

i would like a business card for our security company. i would like the colours to match the logo. or other bright colours can be used. would like it too look professional and smart.

Industry/Entity Type

Security

Contact Information for Business Card

Harbor Crest Security management Tomas Brevik Managing Directorph: 1300 747 433m: 0413 065 438e: tomas@harborcrestsecuritygroup.com.au.auw: www.harborcrestsecuritygroup.com.au

Font styles to use
Serif

Colors
85cae6
0393ce
0655a3
3276b5
fdfdfd
000000
886aae
f04a51
6b449b

Requirements
Must have
• Facebook logo at the back.
• also at the back with bullet points of
• -Concierge
• -public Events
• -Private events
• -Corporate
• -static Guards
• -residential

```html
<!DOCTYPE html>
<html lang="en">
<head>
<meta charset="utf-8">
<title>Harbor Crest Security management – Business Card</title>
<link rel="stylesheet" href="https://fonts.googleapis.com/css2?family=Source+Sans+3:wght@300;400;600;700&display=swap">
<style>
  :root {
    --sky: #85cae6;
    --cyan: #0393ce;
    --navy: #0655a3;
    --mid-blue: #3276b5;
    --bright-blue: #2aa3f0;
    --paper: #fdfdfd;
    --ink: #000000;
    --grey-text: #444444;
    --stage: #e9ecef;
  }
  * { box-sizing: border-box; margin: 0; padding: 0; }
  html, body { width: 1200px; height: 1062px; overflow: hidden; }
  body {
    background: var(--stage);
    font-family: "Source Sans 3", sans-serif;
    position: relative;
  }
  .card {
    position: absolute;
    width: 560px;
    height: 320px;
    border-radius: 4px;
    box-shadow: 0 10px 28px rgba(0,0,0,0.18);
    overflow: hidden;
  }
  /* front */
  .card-front {
    left: 90px; top: 110px;
    background: linear-gradient(160deg, #ffffff 0%, #f1f2f3 100%);
  }
  .front-brand {
    position: absolute; left: 40px; top: 46px;
    display: flex; align-items: center; gap: 14px;
  }
  .brand-dot {
    width: 46px; height: 46px; border-radius: 50%;
    background: var(--bright-blue);
  }
  .brand-name {
    font-weight: 700; font-size: 25px; color: var(--navy);
    line-height: 1.05; max-width: 330px;
  }
  .front-rule {
    position: absolute; left: 0; right: 0; top: 176px;
    height: 7px; background: var(--bright-blue);
  }
  .holder { position: absolute; left: 40px; top: 214px; }
  .holder-name { font-weight: 700; font-size: 26px; color: var(--bright-blue); }
  .holder-title { font-weight: 400; font-size: 19px; color: var(--grey-text); margin-top: 2px; }
  .contacts {
    position: absolute; left: 258px; top: 206px;
    list-style: none; font-size: 14.5px; color: var(--grey-text);
  }
  .contacts li { display: flex; align-items: center; gap: 8px; line-height: 27px; }
  .contacts svg { width: 13px; height: 13px; flex: none; }

  /* back */
  .card-back {
    left: 550px; top: 600px;
    background: linear-gradient(150deg, #1d8fe0 0%, #3cbaf5 55%, #1c8ee2 100%);
  }
  .back-brand {
    position: absolute; right: 34px; top: 30px;
    font-weight: 700; font-size: 30px; color: var(--ink);
    text-align: right; line-height: 1.05; max-width: 300px;
  }
  .services {
    position: absolute; left: 36px; top: 40px; width: 210px;
    list-style: none; font-size: 16px; color: var(--ink);
  }
  .services li {
    display: flex; align-items: center; gap: 8px;
    line-height: 26px; border-bottom: 1px solid rgba(0,0,0,0.35);
  }
  .services li::before {
    content: ""; width: 6px; height: 6px; border-radius: 50%;
    background: var(--ink); flex: none;
  }
  .social {
    position: absolute; left: 36px; top: 222px;
    display: flex; align-items: center; gap: 8px;
    font-size: 16px; color: var(--ink);
  }
  .social-square { width: 16px; height: 16px; background: var(--navy); border-radius: 2px; }
  .back-tag {
    position: absolute; right: 34px; bottom: 30px;
    font-weight: 300; font-size: 15px; letter-spacing: 9px;
    color: rgba(0,0,0,0.55); text-transform: uppercase;
  }
</style>
</head>
<body>

<section class="card card-front" aria-label="Business card front">
  <div class="front-brand">
    <span class="brand-dot"></span>
    <span class="brand-name">Harbor Crest Security management</span>
  </div>
  <div class="front-rule"></div>
  <div class="holder">
    <p class="holder-name">Tomas Brevik</p>
    <p class="holder-title">Managing Director</p>
  </div>
  <ul class="contacts">
    <li>
      <svg viewBox="0 0 16 16"><path d="M4 1l3 3-2 2c1 2 3 4 5 5l2-2 3 3-2 3C7 14 2 9 1 3z" fill="#2aa3f0"/></svg>
      1300 582 916
    </li>
    <li>
      <svg viewBox="0 0 16 16"><circle cx="8" cy="8" r="6.5" fill="none" stroke="#2aa3f0" stroke-width="1.6"/><path d="M1.5 8h13M8 1.5c-3 3.5-3 9.5 0 13M8 1.5c3 3.5 3 9.5 0 13" fill="none" stroke="#2aa3f0" stroke-width="1.2"/></svg>
      www.harborcrestsecuritygroup.com.au
    </li>
    <li>
      <svg viewBox="0 0 16 16"><circle cx="8" cy="8" r="3" fill="none" stroke="#2aa3f0" stroke-width="1.8"/><path d="M11 5v4.5c0 2 3 2 3-1.5A6 6 0 1 0 11 13" fill="none" stroke="#2aa3f0" stroke-width="1.8"/></svg>
      tomas@harborcrestsecuritygroup.com.au
    </li>
  </ul>
</section>

<section class="card card-back" aria-label="Business card back">
  <div class="back-brand">Harbor Crest Security management</div>
  <ul class="services">
    <li>Concierge</li>
    <li>public Events</li>
    <li>Private events</li>
    <li>Corporate</li>
    <li>static Guards</li>
    <li>residential</li>
  </ul>
  <div class="social">
    <span class="social-square"></span>
    www.socialpage.net
  </div>
  <div class="back-tag">Security</div>
</section>

</body>
</html>
```